Business Cards, Stationery, Email signature
and Stationary
Business Cards, Stationery, Email signature - Construction
Creative Brief
Use specific fonts
looking for strong bold lettering
Bright & Fun-filled
Marta Quillen
President
2873 E Marlow Street Orange, CA 94153
marta@larkwoodltdroofing.com
larkwoodltdroofing.com
Was considering having a black business cards so I really wanted to logo to "pop". Even though we are construction I love a card that has personality and fun.

```html
<!DOCTYPE html>
<html lang="en">
<head>
<meta charset="utf-8">
<title>Larkwood Ltd — Business Card</title>
<link href="https://fonts.googleapis.com/css2?family=Cinzel:wght@400;700&family=Lato:wght@700;900&family=Tinos:wght@400;700&display=swap" rel="stylesheet">
<style>
  :root {
    --backdrop: #e9e6e1;
    --card-top: #2a2a2c;
    --card-bottom: #050505;
    --brand-blue: #5fa8d3;
    --name-cyan: #29a9e0;
    --title-gold: #e5b640;
    --text-light: #f2f2f2;
    --icon-blue: #3b9bd8;
    --rule: #8a8a8a;
    --logo-sun: #f2a431;
    --logo-sky: #2f86c8;
  }
  * { margin: 0; padding: 0; box-sizing: border-box; }
  html, body { width: 1200px; height: 780px; overflow: hidden; background: var(--backdrop); }
  .business-card {
    position: absolute; left: 75px; top: 80px; width: 1050px; height: 620px;
    border-radius: 32px;
    background: radial-gradient(ellipse at 30% 10%, var(--card-top) 0%, #151516 45%, var(--card-bottom) 100%);
    box-shadow: 0 14px 36px rgba(0,0,0,.35);
    overflow: hidden;
  }
  .brand { position: absolute; left: 50px; top: 55px; display: flex; align-items: center; }
  .brand-mark {
    width: 140px; height: 140px; border-radius: 50%;
    background: linear-gradient(160deg, var(--logo-sun) 0%, var(--logo-sky) 70%);
  }
  .brand-rule { width: 2px; height: 150px; background: var(--rule); margin: 0 26px 0 22px; }
  .brand-name {
    font-family: "Cinzel", serif; font-weight: 400; font-size: 58px;
    color: var(--brand-blue); letter-spacing: 1px; margin-top: -30px;
  }
  .address {
    position: absolute; left: 130px; top: 285px;
    font-family: "Tinos", serif; font-size: 24px; line-height: 32px; color: var(--text-light);
  }
  .contact-list { position: absolute; left: 80px; top: 370px; list-style: none; }
  .contact-item {
    display: flex; align-items: center; height: 34px;
    font-family: "Tinos", serif; font-size: 24px; color: var(--text-light);
  }
  .contact-item svg { width: 26px; height: 26px; margin-right: 24px; fill: var(--icon-blue); }
  .website {
    position: absolute; left: 70px; top: 545px;
    font-family: "Tinos", serif; font-weight: 700; font-size: 29px;
    color: var(--text-light); letter-spacing: 3px;
  }
  .person { position: absolute; right: 75px; top: 290px; text-align: right; }
  .person-name { font-family: "Lato", sans-serif; font-weight: 900; font-size: 40px; color: var(--name-cyan); }
  .person-title { font-family: "Tinos", serif; font-size: 27px; color: var(--title-gold); margin-top: 2px; }
</style>
</head>
<body>
  <div class="business-card">
    <div class="brand">
      <div class="brand-mark"></div>
      <div class="brand-rule"></div>
      <div class="brand-name">Larkwood Ltd</div>
    </div>

    <div class="address">2873 E Marlow Street<br>Orange, CA 94153</div>

    <ul class="contact-list">
      <li class="contact-item"><svg viewBox="0 0 24 24" aria-hidden="true"></svg>(T) 888-555-0142</li>
      <li class="contact-item"><svg viewBox="0 0 24 24" aria-hidden="true"><path d="M6.6 10.8a15 15 0 0 0 6.6 6.6l2.2-2.2c.3-.3.7-.4 1-.2 1.1.4 2.3.6 3.6.6.6 0 1 .4 1 1V20c0 .6-.4 1-1 1A17 17 0 0 1 3 4c0-.6.4-1 1-1h3.5c.6 0 1 .4 1 1 0 1.3.2 2.5.6 3.6.1.3 0 .7-.2 1z"/></svg>714-555-0187</li>
      <li class="contact-item"><svg viewBox="0 0 24 24" aria-hidden="true"><path d="M7 1h10a2 2 0 0 1 2 2v18a2 2 0 0 1-2 2H7a2 2 0 0 1-2-2V3a2 2 0 0 1 2-2zm0 3v14h10V4zm5 15.5a1.2 1.2 0 1 0 0 2.4 1.2 1.2 0 0 0 0-2.4z"/></svg>714-555-0263</li>
      <li class="contact-item"><svg viewBox="0 0 24 24" aria-hidden="true"><path d="M6 2h12v6H6zM3 9h18a2 2 0 0 1 2 2v7h-5v4H6v-4H1v-7a2 2 0 0 1 2-2zm5 7v4h8v-4z"/></svg>714-555-0318</li>
      <li class="contact-item"><svg viewBox="0 0 24 24" aria-hidden="true"><path d="M2 5h20v14H2zm2 2v.5l8 5 8-5V7zm0 2.8V17h16V9.8l-8 5z"/></svg>marta@larkwoodltdroofing.com</li>
    </ul>

    <div class="website">www.larkwoodltdroofing.com</div>

    <div class="person">
      <div class="person-name">Marta Quillen</div>
      <div class="person-title">President</div>
    </div>
  </div>
</body>
</html>
```